Tranquil Pathway Business Card

Logo attached. (will be printing onto thick white/off white textured card)

Double sided business card for two Therapists working at Tranquil Pathway.

Require one design, but with different name and mobile numbers on each card.

Target Market(s)

Medical, Health

Industry/Entity Type

Business

Contact Information for Business Card

Need one business card design, but a separate card for each person - Colin Marchetti and Marieke de Boeckx.

FRONT OF CARD

Logo

Name (Colin Marchetti on one card, Marieke de Boeckx on the other)
Professional Clinical Hypnotherapist

Consulting Rooms (Near Lindqvist Hospital)
482 Brackenfield Road
Dunmore VIC 3987

Colin@TranquilPathway.example.au OR Marieke@TranquilPathway.example.au

Mobile: 0455 872 604 (for Colin) OR
Mobile: 0467 290 518 (for Marieke)

BACK OF CARD

Logo

Website: www.TranquilPathway.example.au

Phone: 1300 958 471

Requirements
Must have
• Text and logo only. No additiional graphics.

```html
<!DOCTYPE html>
<html lang="en">
<head>
<meta charset="utf-8">
<title>Tranquil Pathway Business Card</title>
<link rel="stylesheet" href="https://fonts.googleapis.com/css2?family=Montserrat:wght@700&family=Roboto:wght@400;500&display=swap">
<style>
  :root {
    --navy: #232c63;
    --grey: #6b6b6b;
    --rule: #8a8a8a;
    --faint: #ecedf1;
    --card: #ffffff;
    --backdrop: #e4e5e8;
    --link: #4a5bc4;
  }
  * { box-sizing: border-box; margin: 0; padding: 0; }
  html, body { width: 1200px; height: 800px; overflow: hidden; }
  body {
    background: var(--backdrop);
    font-family: "Roboto", Arial, sans-serif;
    position: relative;
  }
  .card {
    position: absolute;
    top: 241px;
    width: 520px;
    height: 318px;
    background: var(--card);
    box-shadow: 0 2px 10px rgba(0,0,0,0.12);
    overflow: hidden;
  }
  .card--back { left: 50px; }
  .card--front { left: 630px; }

  .brand {
    position: absolute;
    display: flex;
    align-items: center;
  }
  .brand__dot {
    width: 62px; height: 62px;
    border-radius: 50%;
    background: var(--navy);
    flex: none;
  }
  .brand__divider {
    width: 1px; height: 58px;
    background: var(--rule);
    margin: 0 14px;
  }
  .brand__name {
    font-family: "Montserrat", Arial, sans-serif;
    font-weight: 700;
    color: var(--navy);
    font-size: 25px;
    line-height: 1.05;
    letter-spacing: 0.5px;
    text-transform: uppercase;
  }

  /* back */
  .card--back .brand { left: 118px; top: 92px; }
  .band {
    position: absolute;
    left: 0; right: 0;
    top: 214px;
    height: 32px;
    background: var(--navy);
    color: #fff;
    font-size: 13px;
    display: flex;
    align-items: center;
    padding-left: 40px;
    letter-spacing: 0.3px;
  }
  .band__sep { margin: 0 10px; }

  /* front */
  .card--front .brand { left: 34px; top: 30px; }
  .card--front .brand__dot { width: 56px; height: 56px; }
  .card--front .brand__name { font-size: 22px; }
  .watermark {
    position: absolute;
    right: -30px; top: 90px;
    width: 250px; height: 250px;
    border-radius: 50%;
    background: var(--faint);
  }
  .person { position: absolute; left: 34px; top: 118px; }
  .person__name {
    color: var(--navy);
    font-weight: 500;
    font-size: 16px;
    letter-spacing: 0.6px;
    text-transform: uppercase;
  }
  .person__title { color: var(--grey); font-size: 12px; margin-top: 2px; }
  .address {
    margin-top: 12px;
    color: var(--navy);
    font-size: 12px;
    line-height: 1.4;
  }
  .address__note { color: var(--link); font-style: italic; }
  .rule {
    position: absolute;
    left: 34px; right: 24px; top: 232px;
    height: 1px; background: var(--navy);
  }
  .contacts {
    position: absolute;
    right: 24px; top: 244px;
    list-style: none;
    color: var(--navy);
    font-size: 12px;
    line-height: 1.5;
  }
  .contacts li { display: flex; align-items: center; gap: 7px; }
  .contacts svg { width: 11px; height: 11px; flex: none; }
</style>
</head>
<body>

<section class="card card--back" aria-label="Card back">
  <div class="brand">
    <span class="brand__dot"></span>
    <span class="brand__divider"></span>
    <span class="brand__name">Tranquil<br>Pathway</span>
  </div>
  <div class="band">
    <span>www.TranquilPathway.example.au</span>
    <span class="band__sep">|</span>
    <span>P: 1300 958 471</span>
  </div>
</section>

<section class="card card--front" aria-label="Card front">
  <div class="watermark"></div>
  <div class="brand">
    <span class="brand__dot"></span>
    <span class="brand__divider"></span>
    <span class="brand__name">Tranquil<br>Pathway</span>
  </div>
  <div class="person">
    <p class="person__name">Colin Marchetti</p>
    <p class="person__title">Professional Clinical Hypnotherapist</p>
    <p class="address">
      Consulting Rooms <span class="address__note">(Near Lindqvist Hospital)</span><br>
      482 Brackenfield Road<br>
      Dunmore VIC 3987
    </p>
  </div>
  <div class="rule"></div>
  <ul class="contacts">
    <li>
      <svg viewBox="0 0 12 12"><rect width="12" height="12" rx="2" fill="#777"/><path d="M2 4l4 3 4-3" stroke="#fff" fill="none" stroke-width="1.2"/></svg>
      Colin@TranquilPathway.example.au
    </li>
    <li>
      <svg viewBox="0 0 12 12"><rect width="12" height="12" rx="2" fill="#777"/><rect x="4" y="2" width="4" height="8" rx="1" fill="#fff"/></svg>
      0455 872 604 (for Colin) OR
    </li>
    <li>
      <svg viewBox="0 0 12 12"><rect width="12" height="12" rx="2" fill="#777"/><rect x="4" y="2" width="4" height="8" rx="1" fill="#fff"/></svg>
      0467 290 518 (for Marieke)
    </li>
  </ul>
</section>

</body>
</html>
```